Modern business card for triathlon training business in Australia

We need a business card design for our triathlon training company.

Pace with Us Fitness is an Australian business, owned by women, run for women. Pace with Us Fitness helps women prepare or improve triathlon skills and confidence through triathlon camps completely designed for women.

Our camps focus on preparing women both physically and mentally for their next (or first!) triathlon.

You can see our website www.pacewithusfitness.com.au for more info about our business and our style.

We've attached two of our logos and are happy to consider a design that utilised either colour scheme with the teal colour being our 'feature' colour. We don't want overly feminine cards but rather cards that are professional and neat. If the inclusion of any pictures/art is warranted, this should be focused on our swim/ride/run theme and in that specific order (swim/ride/run).

The business card needs to be a printable design and the contact details will need to change for our two employees.

Target Market(s)

Female clients and partners/vendors/sponsors that we work with in the triathlon industry

Industry/Entity Type

Fitness

Contact Information for Business Card

Pace with Us Fitness (business name)
Nina Carver
Business Director
Mobile: 0438 916 207
Email: nina@pacewithusfitness.com.au
www.pacewithusfitness.com.au

Second business card:
Pace with Us Fitness
Bel Stray
Coaching Director
Mobile: 0459 260 718
Email: bel@pacewithusfitness.com.au

Font styles to use
Serif
Sans Serif

Requirements
Must have
• Core contact details above, our logo and be a printable design
Should not have
• Pink
• Cursive/script fonts

```html
<!DOCTYPE html>
<html lang="en">
<head>
<meta charset="utf-8">
<title>Pace with Us Fitness – Business Card</title>
<link rel="stylesheet" href="https://fonts.googleapis.com/css2?family=Open+Sans:ital,wght@0,700;1,700&display=swap">
<style>
  :root {
    --page: #ffffff;
    --band-dark: #1a9aa8;
    --body-teal: #19bdd0;
    --band-bottom: #1ba2b1;
    --art-light: #1bbbcf;
    --art-deep: #22afc2;
    --ink: #ffffff;
  }
  * { margin: 0; padding: 0; box-sizing: border-box; }
  html, body {
    width: 1200px; height: 720px; overflow: hidden;
    background: var(--page);
    font-family: "Open Sans", Arial, sans-serif;
    color: var(--ink);
  }
  .card {
    position: absolute; left: 40px; top: 40px;
    width: 1120px; height: 640px;
    background: var(--body-teal);
    overflow: hidden;
  }
  .name-band {
    position: absolute; left: 0; top: 0;
    width: 100%; height: 120px;
    background: var(--band-dark);
  }
  .name-gap {
    position: absolute; left: 0; top: 120px;
    width: 100%; height: 14px;
    background: var(--page);
  }
  .sport-art {
    position: absolute; left: 60px; top: 180px;
    width: 1010px; height: 370px;
    background: linear-gradient(90deg, var(--art-light) 0%, var(--art-deep) 55%, var(--art-light) 100%);
  }
  .footer-band {
    position: absolute; left: 0; top: 550px;
    width: 100%; height: 90px;
    background: var(--band-bottom);
  }
  .person-name {
    position: absolute; left: 504px; top: 56px;
    font-size: 44px; font-style: italic; font-weight: 700;
    line-height: 1; letter-spacing: -0.5px;
  }
  .contact {
    position: absolute; left: 506px; top: 148px;
    list-style: none;
    font-size: 32px; font-weight: 700; line-height: 48.5px;
    letter-spacing: -0.3px;
  }
  .brand-mark {
    position: absolute; left: 57px; top: 352px;
    width: 190px; height: 190px;
    border-radius: 50%;
    background: var(--ink);
  }
  .brand-name {
    position: absolute; left: 57px; top: 553px;
    font-size: 33px; font-weight: 700; line-height: 46px;
    letter-spacing: -1px; text-transform: uppercase;
  }
  .website {
    position: absolute; left: 506px; top: 553px;
    font-size: 33px; font-weight: 700; line-height: 48px;
    letter-spacing: -0.3px;
  }
</style>
</head>
<body>
  <div class="card">
    <div class="name-band"></div>
    <div class="name-gap"></div>
    <div class="sport-art" role="img" aria-label="Faint silhouettes of a swimmer, a cyclist and a runner in sequence"></div>
    <div class="footer-band"></div>

    <h1 class="person-name">Bel Stray</h1>
    <ul class="contact">
      <li class="contact-role">Coaching Director</li>
      <li class="contact-phone">0459 260 718</li>
      <li class="contact-email">bel@pacewithusfitness.com.au</li>
    </ul>

    <span class="brand-mark"></span>
    <p class="brand-name">Pace with Us Fitness</p>
    <p class="website">www.pacewithusfitness.com.au</p>
  </div>
</body>
</html>
```